Forest Consultant/Timber Buyer needs a clean business card

We are a forestry consulting and timber buying company. We meet with private landowners and assist them with timber management and timber harvesting. We would like a professional business card, please no clip art. logo is blue and white but would like to see a gray,silver, or some other color incorporated. Would like basic contact info. Would like to the layout to be creative and sleek but masculine.

Target Market(s)

private landowners

Industry/Entity Type

Business

Contact Information for Business Card

name,position, cell number, office number, email, website. This might be to cluttered. Basic contact info is what we are looking for.

Contact info can all be on one side with logo on the other.

Font styles to use
Serif
Sans Serif

Colors
0255a3
ffffff
aaaaaa

Requirements
Must have
• We just want it professional.
Nice to have
• Creative layout.
Should not have
• please no clip art of log trucks etc.

```html
<!DOCTYPE html>
<html lang="en">
<head>
<meta charset="utf-8">
<title>Corvane Forestry — Business Card</title>
<link href="https://fonts.googleapis.com/css2?family=Open+Sans:wght@400;600&display=swap" rel="stylesheet">
<style>
  :root {
    --brand-blue: #0255a3;
    --band-blue: #1f5ea6;
    --white: #ffffff;
    --silver: #aaaaaa;
    --text-gray: #6d6d6d;
    --backdrop: #e4e2de;
  }
  * { box-sizing: border-box; margin: 0; padding: 0; }
  html, body {
    width: 1200px; height: 950px; overflow: hidden;
    background: var(--backdrop);
    font-family: "Open Sans", Arial, sans-serif;
  }
  .sheet {
    width: 1200px; height: 950px;
    display: flex; flex-direction: column; align-items: center; justify-content: center;
    gap: 44px;
  }
  .card {
    width: 700px; height: 400px;
    background: var(--white);
    position: relative;
    box-shadow: 0 6px 18px rgba(0,0,0,0.18);
    overflow: hidden;
  }
  .brand-name {
    color: var(--brand-blue);
    font-weight: 600;
    letter-spacing: 0.5px;
    white-space: nowrap;
  }
  /* Front */
  .card-front .brand {
    position: absolute; left: 0; right: 0; top: 0; height: 250px;
    display: flex; align-items: center; justify-content: center;
  }
  .card-front .brand-name { font-size: 36px; }
  .contact-band {
    position: absolute; left: 0; right: 0; bottom: 0; height: 150px;
    background: var(--band-blue);
    color: var(--white);
    display: flex; align-items: center;
    padding: 0 36px;
  }
  .contact-block { display: flex; flex-direction: column; gap: 6px; }
  .person-name { font-size: 22px; font-weight: 600; letter-spacing: 0.5px; text-transform: uppercase; }
  .person-title { font-size: 14px; letter-spacing: 0.5px; text-transform: uppercase; opacity: 0.9; }
  .contact-line { font-size: 15px; letter-spacing: 0.3px; white-space: nowrap; }
  .divider {
    width: 1px; height: 64px;
    background: var(--silver);
    margin: 0 26px;
    flex: none;
  }
  /* Back */
  .card-back .brand {
    position: absolute; inset: 0;
    display: flex; align-items: center; justify-content: center;
  }
  .card-back .brand-name { font-size: 30px; }
  .back-web {
    position: absolute; left: 36px; bottom: 30px;
    color: var(--text-gray);
    font-size: 14px; letter-spacing: 4px;
  }
</style>
</head>
<body>
<main class="sheet">
  <section class="card card-front" aria-label="Business card front">
    <div class="brand">
      <span class="brand-name">Corvane Forestry</span>
    </div>
    <div class="contact-band">
      <div class="contact-block">
        <span class="person-name">Owen Carter</span>
        <span class="person-title">CEO/Founder</span>
      </div>
      <span class="divider"></span>
      <div class="contact-block">
        <span class="contact-line">P: 555 302 8817</span>
        <span class="contact-line">M: 555 740 1926</span>
      </div>
      <span class="divider"></span>
      <div class="contact-block">
        <span class="contact-line">E: owen@corvaneforestry.com</span>
        <span class="contact-line">W: www.corvaneforestry.com</span>
      </div>
    </div>
  </section>

  <section class="card card-back" aria-label="Business card back">
    <div class="brand">
      <span class="brand-name">Corvane Forestry</span>
    </div>
    <span class="back-web">www.corvaneforestry.com</span>
  </section>
</main>
</body>
</html>
```